Property Management Company looking for a high-end business card, letterhead and envelope design.

We provide high-end / boutique property management for real estate investors or individuals looking for someone to manage their portfolio. we are looking for a cohesive high-end design for our business cards, letterhead and envelopes.

Target Market(s)

Real Estate Investors

Industry/Entity Type

Real Estate

Requirements
Must have
• business card, letterhead and envelope design - logo attached

```html
<!DOCTYPE html>
<html lang="en">
<head>
<meta charset="utf-8">
<title>Halden Property Management – Stationery</title>
<link rel="stylesheet" href="https://fonts.googleapis.com/css2?family=Montserrat:wght@600&family=Lato:wght@400;700&family=Roboto+Condensed:wght@300&display=swap">
<style>
  :root {
    --backdrop: #d9e4ef;
    --paper: #ffffff;
    --navy: #044f80;
    --grey: #a3a3a3;
    --ink: #555a60;
    --muted: #7d8288;
    --shadow: 0 2px 6px rgba(40, 60, 80, 0.35);
  }
  * { box-sizing: border-box; margin: 0; padding: 0; }
  html, body { width: 1200px; height: 831px; overflow: hidden; }
  body { background: var(--backdrop); position: relative; font-family: "Lato", sans-serif; }

  .sheet { position: absolute; background: var(--paper); box-shadow: var(--shadow); overflow: hidden; }

  .brand {
    font-family: "Montserrat", sans-serif;
    font-weight: 600;
    color: var(--navy);
    text-transform: uppercase;
    white-space: nowrap;
    line-height: 1;
  }
  .brand-name { display: block; }
  .brand-tagline { display: block; }

  .contact { color: var(--muted); line-height: 1.35; }
  .contact .row { display: flex; align-items: center; }
  .contact .icon { fill: var(--navy); flex: none; }
  .contact .web strong { color: var(--navy); font-weight: 400; }

  .base-band {
    position: absolute; right: 0; bottom: 0;
    background: linear-gradient(90deg, rgba(163,163,163,0) 0%, var(--grey) 18%, var(--navy) 45%, var(--navy) 100%);
  }

  /* Letterhead */
  .letterhead { left: 117px; top: 111px; width: 430px; height: 609px; }
  .letterhead .brand { position: absolute; left: 39px; top: 37px; }
  .letterhead .brand-name { font-size: 19px; letter-spacing: 0.33em; }
  .letterhead .brand-tagline { font-size: 8.4px; letter-spacing: 0.2em; margin-top: 4px; }
  .letterhead .contact { position: absolute; left: 314px; top: 24px; font-size: 8px; }
  .letterhead .contact .address { margin-bottom: 5px; }
  .letterhead .contact .icon { width: 8px; height: 8px; margin-right: 7px; }
  .letterhead .base-band { width: 62%; height: 14px; }
  .letter-body {
    position: absolute; left: 39px; top: 205px; width: 350px;
    font-family: "Roboto Condensed", sans-serif; font-weight: 300;
    font-size: 9.4px; line-height: 15px; color: var(--ink); text-align: justify;
  }
  .letter-body p { margin-bottom: 15px; }
  .letter-body .greeting { margin-bottom: 13px; }
  .letter-body .closing { margin-top: 37px; margin-bottom: 5px; }
  .signature { display: block; width: 36px; height: 22px; background: linear-gradient(90deg, #dbe5ee, #c7d6e4); border-radius: 2px; }

  /* Business cards */
  .card-front { left: 635px; top: 112px; width: 183px; height: 105px; }
  .card-front .brand { position: absolute; left: 11px; top: 47px; }
  .card-front .brand-name { font-size: 8.6px; letter-spacing: 0.3em; }
  .card-front .brand-tagline { font-size: 3.9px; letter-spacing: 0.17em; margin-top: 1.5px; }
  .card-front .divider { position: absolute; left: 89px; top: 27px; width: 1px; height: 50px; background: var(--navy); }
  .card-front .person { position: absolute; left: 100px; top: 26px; }
  .card-front .person-name { font-weight: 700; font-size: 8.2px; color: var(--navy); text-transform: uppercase; }
  .card-front .person-role { font-size: 4.5px; color: var(--muted); margin-top: 1px; }
  .card-front .contact { position: absolute; left: 100px; top: 46px; font-size: 4.4px; line-height: 1.5; }
  .card-front .contact .address { margin-bottom: 2px; }
  .card-front .contact .icon { width: 4.5px; height: 4.5px; margin-right: 4px; }
  .card-front .base-band { width: 62%; height: 6px; }

  .card-back { left: 904px; top: 111px; width: 182px; height: 104px; background: var(--navy); }
  .card-back .brand { position: absolute; left: 0; right: 0; top: 42px; text-align: center; color: var(--paper); }
  .card-back .brand-name { font-size: 12.5px; letter-spacing: 0.32em; padding-left: 0.32em; }
  .card-back .brand-tagline { font-size: 5.7px; letter-spacing: 0.2em; margin-top: 2px; }

  /* Envelopes */
  .envelope-back { left: 635px; top: 248px; width: 451px; height: 225px; }
  .envelope-back .flap { position: absolute; left: 0; top: 0; width: 451px; height: 66px; }
  .envelope-back .flap path { fill: var(--navy); }

  .envelope-front { left: 635px; top: 494px; width: 451px; height: 226px; }
  .envelope-front .brand { position: absolute; left: 41px; top: 53px; }
  .envelope-front .brand-name { font-size: 19px; letter-spacing: 0.33em; }
  .envelope-front .brand-tagline { font-size: 8.4px; letter-spacing: 0.2em; margin-top: 4px; }
  .envelope-front .contact { position: absolute; left: 42px; top: 152px; font-size: 7.2px; }
  .envelope-front .contact .address { margin-bottom: 3px; }
  .envelope-front .contact .icon { width: 7px; height: 7px; margin-right: 6px; }
  .envelope-front .base-band { width: 62%; height: 14px; }
</style>
</head>
<body>

<svg width="0" height="0" style="position:absolute" aria-hidden="true">
  <defs>
    <symbol id="icon-phone" viewBox="0 0 16 16">
      <path d="M3.5 1.5l2.5-.5 1.5 3.5-1.8 1.3a8 8 0 0 0 4.5 4.5l1.3-1.8 3.5 1.5-.5 2.5C13.5 14 12 14.8 10 14 5.5 12.3 3.7 10.5 2 6 1.2 4 2 2.5 3.5 1.5z"/>
    </symbol>
    <symbol id="icon-mail" viewBox="0 0 16 16">
      <path d="M1 3h14v10H1zM2.5 4.5v.3L8 9l5.5-4.2v-.3zM2.5 6.6v4.9h11V6.6L8 10.8z" fill-rule="evenodd"/>
    </symbol>
    <symbol id="icon-web" viewBox="0 0 16 16">
      <path fill-rule="evenodd" d="M8 1a7 7 0 1 1 0 14A7 7 0 0 1 8 1zm-.6 1.3A5.8 5.8 0 0 0 2.3 7.4h2.6c.1-2 .9-3.8 2.5-5.1zm1.2 0c1.6 1.3 2.4 3.1 2.5 5.1h2.6a5.8 5.8 0 0 0-5.1-5.1zM7.4 3.1C6.5 4.2 6 5.7 6 7.4h1.4zm1.2 0v4.3H10c0-1.7-.5-3.2-1.4-4.3zM2.3 8.6a5.8 5.8 0 0 0 5.1 5.1C5.8 12.4 5 10.6 4.9 8.6zm3.7 0c0 1.7.5 3.2 1.4 4.3V8.6zm2.6 0v4.3c.9-1.1 1.4-2.6 1.4-4.3zm2.5 0c-.1 2-.9 3.8-2.5 5.1a5.8 5.8 0 0 0 5.1-5.1z"/>
    </symbol>
  </defs>
</svg>

<!-- Letterhead -->
<article class="sheet letterhead">
  <div class="brand"><span class="brand-name">Halden</span><span class="brand-tagline">Property Management</span></div>
  <div class="contact">
    <div class="address">1234 First Line Address<br>5678 Second Line Address</div>
    <div class="row"><svg class="icon"><use href="#icon-phone"/></svg>(777) 888-7777</div>
    <div class="row"><svg class="icon"><use href="#icon-mail"/></svg>info@yourmail.com</div>
    <div class="row web"><svg class="icon"><use href="#icon-web"/></svg>www.<strong>yourwebsite</strong>.com</div>
  </div>
  <div class="letter-body">
    <p class="greeting">Dear Sir/Mam,</p>
    <p>Contrary to popular belief, Lorem Ipsum is not simply random text. It has roots in a piece of classical Latin literature from 45 BC, making it over 2000 years old. Richard Marlow, a Latin professor at Ashford College in Vermont, looked up one of the more obscure Latin words, consectetur.</p>
    <p>Lorem Ipsum comes from sections 1.10.32 and 1.10.33 of "de Finibus Bonorum et Malorum" (The Extremes of Good and Evil) by Marcus Vellan, written in 45 BC. This book is a treatise on the theory of ethics, very popular during the Renaissance. The first line of Lorem Ipsum.</p>
    <p>The standard chunk of Lorem Ipsum used since the 1500s is reproduced below for those interested. Sections 1.10.32 and 1.10.33 from "de Finibus Bonorum et Malorum" by Marcus Vellan are also reproduced in their exact original.</p>
    <p>The standard chunk of Lorem Ipsum used since the 1500s is reproduced below for those interested.</p>
    <p class="closing">Best Regards</p>
    <span class="signature" role="img" aria-label="Handwritten signature"></span>
  </div>
  <div class="base-band" role="img" aria-label="Grey and navy accent band"></div>
</article>

<!-- Business card, front -->
<article class="sheet card-front">
  <div class="brand"><span class="brand-name">Halden</span><span class="brand-tagline">Property Management</span></div>
  <div class="divider"></div>
  <div class="person">
    <div class="person-name">Daniel Reyes</div>
    <div class="person-role">Founder &amp; CEO</div>
  </div>
  <div class="contact">
    <div class="address">1234 First Line Address<br>5678 Second Line Address</div>
    <div class="row"><svg class="icon"><use href="#icon-phone"/></svg>(777) 888-7777</div>
    <div class="row"><svg class="icon"><use href="#icon-mail"/></svg>info@yourmail.com</div>
    <div class="row web"><svg class="icon"><use href="#icon-web"/></svg>www.<strong>yourwebsite</strong>.com</div>
  </div>
  <div class="base-band" role="img" aria-label="Grey and navy accent band"></div>
</article>

<!-- Business card, back -->
<article class="sheet card-back">
  <div class="brand"><span class="brand-name">Halden</span><span class="brand-tagline">Property Management</span></div>
</article>

<!-- Envelope, back -->
<article class="sheet envelope-back">
  <svg class="flap" viewBox="0 0 451 66" aria-hidden="true">
    <path d="M0 0 H451 L447 40 C445 55 435 66 420 66 H31 C16 66 6 55 4 40 Z"/>
  </svg>
</article>

<!-- Envelope, front -->
<article class="sheet envelope-front">
  <div class="brand"><span class="brand-name">Halden</span><span class="brand-tagline">Property Management</span></div>
  <div class="contact">
    <div class="address">1234 First Line Address<br>5678 Second Line Address</div>
    <div class="row"><svg class="icon"><use href="#icon-phone"/></svg>(777) 888-7777</div>
    <div class="row"><svg class="icon"><use href="#icon-mail"/></svg>info@yourmail.com</div>
    <div class="row web"><svg class="icon"><use href="#icon-web"/></svg>www.<strong>yourwebsite</strong>.com</div>
  </div>
  <div class="base-band" role="img" aria-label="Grey and navy accent band"></div>
</article>

</body>
</html>
```